businesscard, flyer and membercard

--------------------------------------------------------------------------------------------------
design flyer :
- delivering format (jpg, pdf and original psd)
- there is a example how the flyers should look like
the text and logo should be the same as the exemple flyer, the creativity is yours.
- the design should have a back and front side.
File format : 15,0 cm x 21,2 cm
design membercard :
- there is example how the member-card should look like
the text and logo should be the same as the exemple membercard, the creativity is yours.
- the front side contains text and open space where for writing :
Naam ......
Dansstijlen ......
- the front side contains 12 circels horizontal at the line name at the end of the line "Salsa".
- the front side contains 12 circels horizontal at the line name at the end of the line "Bachata".
- the front side contains 12 circels horizontal at the line name at the end of the line "Kizomba".
- each horizontal line with circels contains a different kind of color/design.
- file format: 7,6 cm x 10,7 cm
Business card :
- there is example how the businesscard should look like
the text and logo should be the same as the exemple buisinesscard, the creativity is yours.
- the design should have a back a front side
File format : 8,7 cm x 5,7 cm

Target Market(s)

Dancing :Salsa, Bachata and Kizomba

Colors

Designer to choose colors to be used in the design.

Requirements
Must have
• same text as seen on the examples.
Nice to have
• see the examples as attachments
Should not have
• - REMOVE TEXT "KOV" from the design
• - REMOVE TEXT "Gratis Parkeren"

```html
<!DOCTYPE html>
<html lang="nl">
<head>
<meta charset="utf-8">
<title>Vela Dance Studio – Flyers</title>
<link href="https://fonts.googleapis.com/css2?family=Cinzel:wght@400;700&family=Montserrat:wght@400;600&family=Roboto+Condensed:wght@400&display=swap" rel="stylesheet">
<style>
  :root {
    --stage: #140205;
    --ink-dark: #1a0a0c;
    --gold: #f3d79a;
    --gold-deep: #c9a25a;
    --cream: #fff3dc;
    --red: #c4202c;
    --circle: #fbd97a;
    --white: #ffffff;
  }
  * { margin: 0; padding: 0; box-sizing: border-box; }
  html, body { width: 1200px; height: 1200px; overflow: hidden; background: var(--stage); }
  .canvas { position: relative; width: 1200px; height: 1200px; background: var(--stage); }

  .flyer { position: absolute; width: 582px; height: 751px; overflow: hidden; color: var(--white); }
  .flyer--schedule { left: 5px; top: 26px; }
  .flyer--trial { left: 600px; top: 402px; }

  .flyer__bg { position: absolute; inset: 0; width: 100%; height: 100%; }
  .abs { position: absolute; }
  .center { left: 0; right: 0; text-align: center; }

  .studio-name { font-family: 'Cinzel', serif; font-weight: 700; color: var(--white); letter-spacing: 6px; }
  .studio-sub { font-family: 'Montserrat', sans-serif; font-weight: 600; color: var(--white); letter-spacing: 1px; }

  .headline { font-family: 'Cinzel', serif; color: var(--gold); text-shadow: 0 2px 4px rgba(0,0,0,.5); }

  .badge { font-family: 'Cinzel', serif; color: var(--ink-dark); font-size: 17px; line-height: 20px; text-align: center;
           transform: rotate(27deg); left: 440px; top: 72px; width: 140px; }

  .class-photo { position: absolute; width: 158px; height: 158px; border-radius: 50%;
                 background: radial-gradient(circle at 50% 45%, #fde49a 0%, var(--circle) 55%, #e9b64f 100%); top: 285px; }

  .day { font-family: 'Cinzel', serif; font-size: 21px; top: 478px; color: var(--cream); }
  .slots { font-family: 'Cinzel', serif; font-size: 14.5px; line-height: 20px; color: var(--gold); top: 514px; }
  .slots span { display: inline-block; width: 22px; text-align: right; }
  .divider { width: 1px; height: 88px; top: 495px; background: linear-gradient(var(--gold-deep), transparent); }

  .styles { font-family: 'Cinzel', serif; font-size: 19px; letter-spacing: 9px; color: var(--cream); }
  .styles b { font-weight: 400; display: inline-block; margin: 0 14px; }

  .venue { font-family: 'Cinzel', serif; font-size: 40px; color: var(--gold); top: 628px; letter-spacing: 1px; }

  .contact { font-family: 'Roboto Condensed', sans-serif; font-size: 12.5px; color: var(--white);
             display: flex; align-items: center; justify-content: center; gap: 22px; }
  .contact__item { display: flex; align-items: center; gap: 8px; }
  .contact__icon { width: 28px; height: 28px; border-radius: 50%; background: var(--gold-deep); display: flex; align-items: center; justify-content: center; }

  .date-band { top: 450px; height: 30px; background: linear-gradient(90deg, transparent, rgba(40,20,40,.85) 20%, rgba(40,20,40,.85) 80%, transparent);
               border-top: 1px solid rgba(243,215,154,.5); border-bottom: 1px solid rgba(243,215,154,.5);
               font-family: 'Cinzel', serif; font-size: 22px; line-height: 28px; color: var(--gold); }
  .perks { font-family: 'Montserrat', sans-serif; font-size: 13px; letter-spacing: 3px; line-height: 19px; color: var(--cream); top: 577px; }
</style>
</head>
<body>
<main class="canvas">

  <!-- Schedule flyer -->
  <section class="flyer flyer--schedule">
    <svg class="flyer__bg" viewBox="0 0 582 751" role="img" aria-label="Ballroom couple dancing against a glowing stage light backdrop">
      <defs>
        <linearGradient id="sch-base" x1="0" y1="0" x2="1" y2="1">
          <stop offset="0" stop-color="#3b2f8f"/>
          <stop offset=".45" stop-color="#8a2d6a"/>
          <stop offset=".7" stop-color="#b32b3a"/>
          <stop offset="1" stop-color="#2a0c10"/>
        </linearGradient>
        <radialGradient id="sch-flare" cx=".85" cy=".1" r=".5">
          <stop offset="0" stop-color="#ffe9b8"/>
          <stop offset=".4" stop-color="#f59a5a" stop-opacity=".7"/>
          <stop offset="1" stop-color="#f59a5a" stop-opacity="0"/>
        </radialGradient>
        <linearGradient id="sch-fade" x1="0" y1="0" x2="0" y2="1">
          <stop offset=".45" stop-color="#1c0a0d" stop-opacity="0"/>
          <stop offset=".72" stop-color="#1c0a0d" stop-opacity=".9"/>
          <stop offset="1" stop-color="#1c0a0d"/>
        </linearGradient>
      </defs>
      <rect width="582" height="751" fill="url(#sch-base)"/>
      <rect width="582" height="751" fill="url(#sch-flare)"/>
      <rect width="582" height="751" fill="url(#sch-fade)"/>
      <path d="M0 645 Q291 720 582 645 L582 751 L0 751 Z" fill="#8d1722"/>
      <path d="M0 660 Q291 728 582 660 L582 751 L0 751 Z" fill="#2a1215"/>
      <path d="M0 660 Q291 728 582 660" fill="none" stroke="#d9a65a" stroke-width="1.2"/>
    </svg>

    <div class="abs center studio-name" style="top:62px;font-size:38px;">VELA</div>
    <div class="abs center studio-sub" style="top:138px;font-size:15px;">DANCE STUDIO</div>
    <div class="abs badge">ALTIJD<br>EERSTE LES<br>GRATIS</div>

    <div class="abs center headline" style="top:205px;font-size:58px;">LES ROOSTER</div>

    <div class="class-photo" style="left:51px;" role="img" aria-label="Couple dancing salsa, woman in red dress"></div>
    <div class="class-photo" style="left:219px;" role="img" aria-label="Couple dancing kizomba, woman in red dress"></div>
    <div class="class-photo" style="left:387px;" role="img" aria-label="Couple dancing bachata, woman in red dress"></div>

    <div class="abs day" style="left:55px;">DINSDAG</div>
    <div class="abs day" style="left:215px;">WOSNSDAG</div>
    <div class="abs day" style="left:385px;">DONDERDA</div>

    <div class="abs slots" style="left:58px;">19:00 SALSA <span style="width:44px">1</span><br>20:00 SALSA <span style="width:44px">3</span><br>21:00 BACGATA <span>3</span></div>
    <div class="abs divider" style="left:193px;"></div>
    <div class="abs slots" style="left:211px;">19:00 KIZOMBA <span style="width:24px">2</span><br>20:00 KIZOMBA <span style="width:24px">1</span><br>21:00 KIZOMBA <span style="width:24px">3</span></div>
    <div class="abs divider" style="left:362px;"></div>
    <div class="abs slots" style="left:385px;">19:00 SALSA <span style="width:44px">2</span><br>20:00 BACGATA <span style="width:14px">1</span><br>21:00 BACGATA <span style="width:14px">2</span></div>

    <div class="abs center styles" style="top:593px;"><b>SALSA</b><b>BACHATA</b><b>KIZOMBA</b></div>
    <div class="abs center venue">CLUB ORVANO</div>

    <div class="abs center contact" style="top:709px;">
      <div class="contact__item">
        <span class="contact__icon"><svg width="14" height="16" viewBox="0 0 14 18"><path d="M7 0C3 0 0 3 0 7c0 5 7 11 7 11s7-6 7-11c0-4-3-7-7-7zm0 10a3 3 0 1 1 0-6 3 3 0 0 1 0 6z" fill="#fff"/></svg></span>
        Kadeweg 14, 2500 AB Den Haag
      </div>
      <div class="contact__item"><span class="contact__icon"></span>Veladenhaag</div>
      <div class="contact__item">
        <span class="contact__icon"><svg width="14" height="14" viewBox="0 0 24 24"><path d="M6.6 10.8a15 15 0 0 0 6.6 6.6l2.2-2.2c.3-.3.7-.4 1-.2 1.1.4 2.3.6 3.6.6.6 0 1 .4 1 1V20c0 .6-.4 1-1 1C10.6 21 3 13.4 3 4c0-.6.4-1 1-1h3.5c.6 0 1 .4 1 1 0 1.3.2 2.5.6 3.6.1.3 0 .7-.2 1z" fill="#fff"/></svg></span>
        0612345678
      </div>
    </div>
  </section>

  <!-- Trial lessons flyer -->
  <section class="flyer flyer--trial">
    <svg class="flyer__bg" viewBox="0 0 582 751" role="img" aria-label="Dancing couple in motion, man in tuxedo and woman with flowing red hair, under coloured stage lights">
      <defs>
        <linearGradient id="tr-base" x1="0" y1="0" x2="1" y2="1">
          <stop offset="0" stop-color="#24103a"/>
          <stop offset=".5" stop-color="#5a2a7a"/>
          <stop offset=".8" stop-color="#a62a55"/>
          <stop offset="1" stop-color="#2a0c14"/>
        </linearGradient>
        <radialGradient id="tr-glow" cx=".3" cy=".6" r=".45">
          <stop offset="0" stop-color="#5a8fe0" stop-opacity=".8"/>
          <stop offset="1" stop-color="#5a8fe0" stop-opacity="0"/>
        </radialGradient>
        <radialGradient id="tr-flare" cx=".95" cy=".15" r=".4">
          <stop offset="0" stop-color="#ff9aa5" stop-opacity=".8"/>
          <stop offset="1" stop-color="#ff9aa5" stop-opacity="0"/>
        </radialGradient>
        <radialGradient id="tr-figure" cx=".5" cy=".55" r=".35">
          <stop offset="0" stop-color="#180812" stop-opacity=".85"/>
          <stop offset="1" stop-color="#180812" stop-opacity="0"/>
        </radialGradient>
      </defs>
      <rect width="582" height="751" fill="url(#tr-base)"/>
      <rect width="582" height="751" fill="url(#tr-glow)"/>
      <rect width="582" height="751" fill="url(#tr-flare)"/>
      <rect width="582" height="751" fill="url(#tr-figure)"/>
      <path d="M0 640 Q291 700 582 640 L582 751 L0 751 Z" fill="#8d1722"/>
      <path d="M0 652 Q291 712 582 652 L582 751 L0 751 Z" fill="#24101a"/>
      <path d="M0 652 Q291 712 582 652" fill="none" stroke="#d9a65a" stroke-width="1.2"/>
    </svg>

    <div class="abs center studio-name" style="top:148px;font-size:38px;top:140px;">VELA</div>
    <div class="abs center studio-sub" style="top:208px;font-size:20px;top:206px;">DANCE STUDIO</div>

    <div class="abs center headline" style="top:340px;font-size:60px;line-height:60px;">GRATIS</div>
    <div class="abs center headline" style="top:393px;font-size:60px;line-height:60px;">PROEFLESSEN</div>

    <div class="abs center date-band">26 T/M SEPT</div>

    <div class="abs center styles" style="top:493px;"><b>SALSA</b><b>BACHATA</b><b>KIZOMBA</b></div>

    <div class="abs center perks">EERSTE LES GRATIS<br>STUDENTE KORTING<br>ELK NIVEAU<br>ALLE LEEFTIJDEN</div>

    <div class="abs center contact" style="top:701px;">
      <div class="contact__item">
        <span class="contact__icon"><svg width="14" height="16" viewBox="0 0 14 18"><path d="M7 0C3 0 0 3 0 7c0 5 7 11 7 11s7-6 7-11c0-4-3-7-7-7zm0 10a3 3 0 1 1 0-6 3 3 0 0 1 0 6z" fill="#fff"/></svg></span>
        Kadeweg 14, 2500 AB Den Haag
      </div>
      <div class="contact__item"><span class="contact__icon"></span>Veladenhaag</div>
      <div class="contact__item">
        <span class="contact__icon"><svg width="14" height="14" viewBox="0 0 24 24"><path d="M6.6 10.8a15 15 0 0 0 6.6 6.6l2.2-2.2c.3-.3.7-.4 1-.2 1.1.4 2.3.6 3.6.6.6 0 1 .4 1 1V20c0 .6-.4 1-1 1C10.6 21 3 13.4 3 4c0-.6.4-1 1-1h3.5c.6 0 1 .4 1 1 0 1.3.2 2.5.6 3.6.1.3 0 .7-.2 1z" fill="#fff"/></svg></span>
        0612345678
      </div>
    </div>
  </section>

</main>
</body>
</html>
```